Legal Service Estimated Retainer and Average Case Value

We need an 11x14 flyer that contains the standard retainers and average cost be case, both provided in documents, for each case type we handle. We need the information displayed, preferably in a way that makes the information readable but less troubling to a client shocked at price of litigation. We need one sheet with the retainers and average case value merged into one table.

Target Market(s)

Potential Clients

Font styles to use
Serif
Sans Serif

```html
<!DOCTYPE html>
<html lang="en">
<head>
<meta charset="utf-8">
<title>Law Office of Marcus T Hollander – Fees and Retainers Flyer</title>
<link rel="stylesheet" href="https://fonts.googleapis.com/css2?family=Cinzel:wght@600;700;800&family=Open+Sans:wght@400;600&display=swap">
<style>
  :root {
    --navy: #1b1f4b;
    --navy-deep: #12153a;
    --orange: #f26b1d;
    --white: #ffffff;
    --paper: #f7f7f8;
    --ink: #2b2d3f;
    --backdrop: #d6d6d8;
    --statue-light: #8d8fa6;
    --statue-mid: #4b4d6e;
  }
  * { box-sizing: border-box; margin: 0; padding: 0; }
  html, body { width: 1200px; height: 960px; overflow: hidden; }
  body {
    background: var(--backdrop);
    display: flex; align-items: center; justify-content: center;
    font-family: "Open Sans", Arial, sans-serif;
    color: var(--ink);
  }
  .flyer {
    width: 1120px; height: 880px;
    background: var(--paper);
    display: flex; flex-direction: column;
    box-shadow: 0 6px 18px rgba(0,0,0,.18);
  }

  /* Header */
  .masthead {
    height: 96px; padding: 0 48px;
    display: flex; align-items: center; justify-content: space-between;
    background: var(--white);
  }
  .firm-name { display: flex; align-items: center; gap: 14px; }
  .firm-name__mark { width: 16px; height: 16px; background: var(--navy); }
  .firm-name__text {
    font-family: "Cinzel", Georgia, serif; font-weight: 700;
    color: var(--navy); font-size: 30px; line-height: 1.05;
  }
  .firm-name__text small { display: block; font-size: 13px; letter-spacing: .5px; }
  .consult { display: flex; align-items: center; gap: 14px; }
  .consult__icon {
    width: 44px; height: 44px; border-radius: 50%; background: var(--navy);
    display: flex; align-items: center; justify-content: center;
  }
  .consult__text { font-family: "Cinzel", Georgia, serif; line-height: 1.1; }
  .consult__label { color: var(--orange); font-weight: 700; font-size: 14px; }
  .consult__phone { color: var(--navy); font-weight: 800; font-size: 28px; }
  .consult__cta { color: var(--navy); font-weight: 700; font-size: 13px; }

  /* Hero */
  .hero {
    position: relative; height: 300px;
    background: linear-gradient(120deg, var(--navy-deep), var(--navy) 60%, #272b58);
    display: flex;
  }
  .hero__photo {
    width: 560px; height: 100%;
    background:
      radial-gradient(ellipse at 45% 55%, var(--statue-light) 0%, var(--statue-mid) 45%, transparent 75%),
      linear-gradient(90deg, #6f7190 0%, var(--statue-mid) 55%, var(--navy) 100%);
  }
  .hero__copy {
    flex: 1; display: flex; flex-direction: column;
    align-items: center; justify-content: center; gap: 22px;
  }
  .slogan {
    font-family: "Cinzel", Georgia, serif; font-weight: 700;
    color: var(--white); font-size: 54px; line-height: 1.08; text-align: left;
  }
  .slogan__accent { color: var(--orange); }
  .website { display: flex; align-items: center; gap: 12px; color: var(--white); font-size: 18px; }

  /* Fee tables */
  .fees {
    flex: 1; background: var(--white);
    padding: 26px 48px 14px;
    display: grid; grid-template-columns: 1fr 1fr; column-gap: 48px;
    grid-template-rows: 1fr auto;
  }
  .fee-block__title {
    font-family: "Cinzel", Georgia, serif; font-weight: 700; color: var(--navy);
    font-size: 22px; line-height: 1.1;
    border-left: 6px solid var(--orange); padding-left: 12px; margin-bottom: 12px;
  }
  .fee-list { list-style: none; font-size: 13px; line-height: 19px; }
  .disclaimer {
    grid-column: 1 / -1; color: var(--orange); font-size: 13px; line-height: 18px;
    text-align: center; padding-top: 8px;
  }

  /* Footer */
  .contact-bar {
    height: 84px; background: var(--navy); color: var(--white);
    display: flex; align-items: center; justify-content: space-between;
    padding: 0 48px; font-size: 19px;
  }
  .contact-bar__item { display: flex; align-items: center; gap: 12px; }
</style>
</head>
<body>
  <main class="flyer">
    <header class="masthead">
      <div class="firm-name">
        <span class="firm-name__mark"></span>
        <div class="firm-name__text"><small>The Law Office of</small>Marcus T Hollander</div>
      </div>
      <div class="consult">
        <span class="consult__icon">
          <svg width="22" height="22" viewBox="0 0 24 24" fill="none" stroke="#ffffff" stroke-width="2" stroke-linecap="round" stroke-linejoin="round"><path d="M5 3h4l2 5-2.5 1.5a11 11 0 0 0 6 6L16 13l5 2v4a2 2 0 0 1-2 2A16 16 0 0 1 3 5a2 2 0 0 1 2-2z"/></svg>
        </span>
        <div class="consult__text">
          <div class="consult__label">Free Consultation</div>
          <div class="consult__phone">800-555-0142</div>
          <div class="consult__cta">Call Now</div>
        </div>
      </div>
    </header>

    <section class="hero">
      <div class="hero__photo" role="img" aria-label="Photograph of a bronze Lady Justice statue holding scales, in soft blue light"></div>
      <div class="hero__copy">
        <h1 class="slogan">You Talk<br>We Listen<br><span class="slogan__accent">You Win</span></h1>
        <div class="website">
          <svg width="26" height="26" viewBox="0 0 24 24" fill="none" stroke="#ffffff" stroke-width="1.6"><circle cx="12" cy="12" r="10"/><ellipse cx="12" cy="12" rx="4.5" ry="10"/><path d="M2 12h20M4 7h16M4 17h16"/></svg>
          <span>www.hollanderfamilylaw.com</span>
        </div>
      </div>
    </section>

    <section class="fees">
      <div class="fee-block">
        <h2 class="fee-block__title">Average Fee<br>Per Case Type</h2>
        <ul class="fee-list">
          <li>Custody Contempt/Modification $5,000 - $8,000</li>
          <li>Custody Initial Order $4,000 - $7,000</li>
          <li>Custody &amp; Support $5,000 - $8,000</li>
          <li>Support $2,000 - $4,000</li>
          <li>Divorce (3301c) $1,500 - $3,000</li>
          <li>Divorce (3301d) $2,000 - $3,000</li>
          <li>Protection From Abuse $1,500 - $3,000</li>
          <li>Divorce &amp; Custody $5,000 - $8,000</li>
          <li>Divorce &amp; Equitable Distribution $6,000 - $10,000</li>
          <li>Divorce, Custody &amp; Support $8,000 - $12,000</li>
          <li>Divorce, Equitable Distribution &amp; Custody $10,000 - $15,000</li>
          <li>Divorce, Equitable Distribution &amp; Support $8,000 - $12,000</li>
          <li>Divorce, Equitable Distribution, Custody &amp; Support $12,000 - $15,000</li>
        </ul>
      </div>
      <div class="fee-block">
        <h2 class="fee-block__title">Retainers and Total<br>Estimated Case Costs</h2>
        <ul class="fee-list">
          <li>Divorce (3301 C): Retainer: $2,000</li>
          <li>Divorce (3301 D): Retainer: $2,500</li>
          <li>Divorce and Custody: Retainer: $3,500</li>
          <li>Divorce and Equitable Distribution: Retainer: $3,500</li>
          <li>Divorce and Support: Retainer: $3,000</li>
          <li>Divorce, Custody and Support: Retainer: $3,500</li>
          <li>Divorce, Equitable Distribution and Support: Retainer: $3,500</li>
          <li>Divorce, Equitable Distribution and Custody: Retainer: $5,000</li>
          <li>Divorce, Equitable Distribution, Custody and Support: Retainer: $3,500</li>
          <li>Custody Initial Order: Retainer: $3,000</li>
          <li>Custody Modification: Retainer: $3,500</li>
          <li>Custody and Support: Retainer: $3,000</li>
          <li>(PFA) Protection From Abuse: $2,000 Paid In Full</li>
        </ul>
      </div>
      <p class="disclaimer">In order for our clients to set expectations for legal fees, we provide the national average range of fees per case type. These are only to provide you with an understanding of what other cases have cost clients in similar cases. Please note these are not estimates nor guarantees of your own legal costs.</p>
    </section>

    <footer class="contact-bar">
      <div class="contact-bar__item">
        <svg width="22" height="26" viewBox="0 0 24 28" fill="#ffffff"><path d="M12 0C6 0 1.5 4.5 1.5 10.2 1.5 17.5 12 28 12 28s10.5-10.5 10.5-17.8C22.5 4.5 18 0 12 0zm0 14.5a4.3 4.3 0 1 1 0-8.6 4.3 4.3 0 0 1 0 8.6z"/></svg>
        <span>48 Alder Row, Fairmont Hills, VA, 24502</span>
      </div>
      <div class="contact-bar__item">
        <svg width="30" height="22" viewBox="0 0 30 22" fill="none" stroke="#ffffff" stroke-width="2"><rect x="1" y="1" width="28" height="20"/><path d="M1 1l14 11L29 1M1 21l10-10M29 21L19 11"/></svg>
        <span>contact@hollanderfamilylaw.com</span>
      </div>
    </footer>
  </main>
</body>
</html>
```